Veranaxis Business Card and Letter Head

We are a leadership assessment consultancy based in Sydney, Australia. We help executive-level decison-makers select leaders for more senior level roles in corporate and government organisations. Our methodology is based on the latest research from the field of neuroscience.
We need a business card design and matching letter head that presents our company, Veranaxis, as a:
1. trusted adviser to senior executive-level decison makers
2. niche consultancy who are experts in the field of assessing leadership talent
3. results-focused solution provider who balance scientific methods with pragmatic solutions
The following company details should be used in all designs:
Company Name: Veranaxis
Details (for business card):
Daniel Prescott
Senior Talent Adviser
Level 29, Brenning Tower
7 Brenning Square
Sydney, NSW 2000 Australia
Phone: 1300 482 716
Mobile: 0412 573 208
Email: daniel.prescott@veranaxis.com.au
Website: veranaxis.com.au
I have attached the logo for Veranaxis (for both a white and black background) - your business card and letter head designs must incoporate this logo and colour scheme.
Thanks for your interest in this project, I'm looking forward to receiving your ideas.
Regards,
Daniel
Executive-level decison-makers in corporate and government organisations (e.g., CEO, VP, Head of Human Resources)
Leadership

```html
<!DOCTYPE html>
<html lang="en">
<head>
<meta charset="utf-8">
<title>Veranaxis Stationery</title>
<link rel="stylesheet" href="https://fonts.googleapis.com/css2?family=Roboto+Condensed:wght@400;700&display=swap">
<style>
  :root {
    --page: #ffffff;
    --backdrop: #ffffff;
    --ink: #1a1a1a;
    --accent: #c0462a;
    --card-light: #d3d4d6;
    --card-dark: #231f20;
    --frame-light: #ffffff;
    --frame-dark: #d9d9d9;
    --muted: #3a3a3a;
  }
  * { margin: 0; padding: 0; box-sizing: border-box; }
  html, body { width: 1144px; height: 1200px; overflow: hidden; background: var(--backdrop); }
  body { position: relative; font-family: "Roboto Condensed", "Arial Narrow", sans-serif; color: var(--ink); }

  .letterhead {
    position: absolute; left: 40px; top: 38px; width: 784px; height: 1148px;
    background: var(--page);
    box-shadow: 0 2px 10px rgba(0,0,0,.22);
  }

  .brand { display: flex; align-items: center; gap: 10px; }
  .brand-square { width: 26px; height: 26px; background: var(--accent); flex: none; }
  .brand-name { font-weight: 700; font-size: 36px; line-height: 1; letter-spacing: -0.3px; }

  .letterhead .brand { position: absolute; left: 0; right: 0; top: 70px; justify-content: center; }
  .letterhead .brand-name { color: var(--ink); }

  .letter-footer {
    position: absolute; left: 0; right: 0; bottom: 26px;
    text-align: center; font-size: 12px; line-height: 16px; color: var(--ink);
  }
  .letter-footer .label { color: var(--accent); }

  .card {
    position: absolute; width: 372px; height: 228px;
    box-shadow: 0 1px 4px rgba(0,0,0,.2);
  }
  .card--light { background: var(--card-light); }
  .card--dark { background: var(--card-dark); }
  .card-frame { position: absolute; inset: 0; }

  .card-front .brand { position: absolute; inset: 0; justify-content: center; }
  .card-front .brand-name { font-size: 34px; }
  .card--light .brand-name { color: var(--ink); }
  .card--dark .brand-name { color: #ffffff; }

  .card-back .details { position: absolute; left: 54px; top: 40px; font-size: 10.5px; line-height: 15px; }
  .details .person { color: var(--accent); font-weight: 700; font-size: 11.5px; line-height: 15px; }
  .details .role { font-weight: 700; font-size: 11.5px; margin-bottom: 9px; }
  .details .address { margin-bottom: 9px; }
  .details .label { color: var(--accent); display: inline-block; width: 12px; }
  .card--light .details { color: var(--muted); }
  .card--light .details .role { color: var(--ink); }
  .card--dark .details { color: #d6d6d6; }
  .card--dark .details .role { color: #ffffff; }
</style>
</head>
<body>

<section class="letterhead">
  <div class="brand">
    <span class="brand-square"></span>
    <span class="brand-name">Veranaxis</span>
  </div>

  <footer class="letter-footer">
    <div>Level 29, Brenning Tower, 7 Brenning Square, Sydney, NSW 2000 Australia</div>
    <div><span class="label">T:</span> 1300 482 716 | <span class="label">M:</span> 0412 573 208 | <span class="label">E:</span> daniel.prescott@veranaxis.com.au | <span class="label">W:</span> www.veranaxis.com.au</div>
  </footer>
</section>

<article class="card card--light card-front" style="left:366px; top:350px;">
  <svg class="card-frame" viewBox="0 0 372 228">
    <rect x="22" y="26" width="328" height="176" fill="none" stroke="var(--frame-light)" stroke-width="1.5"/>
  </svg>
  <div class="brand">
    <span class="brand-square"></span>
    <span class="brand-name">Veranaxis</span>
  </div>
</article>

<article class="card card--light card-back" style="left:748px; top:350px;">
  <svg class="card-frame" viewBox="0 0 372 228">
    <rect x="22" y="26" width="328" height="176" fill="none" stroke="var(--frame-light)" stroke-width="1.5"/>
  </svg>
  <div class="details">
    <div class="person">Daniel Prescott</div>
    <div class="role">Senior Talent Adviser</div>
    <div class="address">Level 29, Brenning Tower, 7 Brenning Square<br>Sydney, NSW 2000 Australia</div>
    <div><span class="label">T</span>: 1300 482 716</div>
    <div><span class="label">M</span>: 0412 573 208</div>
    <div><span class="label">E</span>: daniel.prescott@veranaxis.com.au</div>
    <div><span class="label">W</span>: www.veranaxis.com.au</div>
  </div>
</article>

<article class="card card--dark card-front" style="left:366px; top:590px;">
  <svg class="card-frame" viewBox="0 0 372 228">
    <rect x="22" y="26" width="328" height="176" fill="none" stroke="var(--frame-dark)" stroke-width="1.5"/>
  </svg>
  <div class="brand">
    <span class="brand-square"></span>
    <span class="brand-name">Veranaxis</span>
  </div>
</article>

<article class="card card--dark card-back" style="left:748px; top:590px;">
  <svg class="card-frame" viewBox="0 0 372 228">
    <rect x="22" y="26" width="328" height="176" fill="none" stroke="var(--frame-dark)" stroke-width="1.5"/>
  </svg>
  <div class="details">
    <div class="person">Daniel Prescott</div>
    <div class="role">Senior Talent Adviser</div>
    <div class="address">Level 29, Brenning Tower, 7 Brenning Square<br>Sydney, NSW 2000 Australia</div>
    <div><span class="label">T</span>: 1300 482 716</div>
    <div><span class="label">M</span>: 0412 573 208</div>
    <div><span class="label">E</span>: daniel.prescott@veranaxis.com.au</div>
    <div><span class="label">W</span>: www.veranaxis.com.au</div>
  </div>
</article>

</body>
</html>
```